Business card for Full Stable Care Vandorpe

I would like to have me designed an professional business card with my existing logo for my company called : full stable care vandorpe gcv.
I prefer a two sided business card with on the back side only the horses head and the website : fscvandorpe-example.eu
Only one colour shouldbe all right.
The logo must appear in a nic professional way on the business card.

Other suggestion are welcome.

All copy wrights must be released by the designer after we have selected a final design.

Target Market(s)

Equestrian businesses

Industry/Entity Type

Business

Contact Information for Business Card

Laurent Vandorpe
Title: zaakvoerder
Full Stable Care Vandorpe GCV
Molkenweg 47
B - 2890 Lindenhoven
België
Phone: + 32 491 68 27 04
Mail: laurent@fscvandorpe-example.eu

Font styles to use
Serif

Requirements
Must have
• My own logo
• See attached files
• Website: fscvandorpe-example.eu

```html
<!DOCTYPE html>
<html lang="en">
<head>
<meta charset="utf-8">
<title>Full Stable Care Vandorpe – Business Card</title>
<link href="https://fonts.googleapis.com/css2?family=Lato:wght@400;700&display=swap" rel="stylesheet">
<style>
  :root {
    --stage: #2a2b30;
    --paper: #ffffff;
    --ink: #111111;
    --ink-soft: #3a3a3a;
    --rule: #8a8a8a;
    --band: #0b0b0b;
  }
  * { margin: 0; padding: 0; box-sizing: border-box; }
  html, body {
    width: 1200px; height: 900px; overflow: hidden;
    background: var(--stage);
    font-family: "Lato", Arial, sans-serif;
  }
  .canvas {
    width: 1200px; height: 900px;
    display: flex; flex-direction: column;
    align-items: center; justify-content: center; gap: 56px;
  }
  .card {
    width: 600px; height: 343px;
    position: relative; overflow: hidden;
  }
  /* Front */
  .card--front { background: var(--paper); color: var(--ink); }
  .brand {
    position: absolute; left: 44px; top: 118px; width: 260px;
    display: flex; align-items: center; gap: 12px;
  }
  .brand__dot {
    width: 16px; height: 16px; border-radius: 50%;
    background: var(--ink); flex: none;
  }
  .brand__name {
    font-weight: 700; font-size: 21px; line-height: 1.2;
    text-transform: uppercase; letter-spacing: 0.5px;
  }
  .divider {
    position: absolute; left: 320px; top: 40px;
    width: 1px; height: 200px; background: var(--rule);
  }
  .contact { position: absolute; left: 346px; top: 48px; width: 240px; }
  .contact__name {
    font-weight: 700; font-size: 16px; letter-spacing: 0.4px;
    text-transform: uppercase;
  }
  .contact__title { font-weight: 700; font-size: 11px; margin-top: 2px; }
  .contact__address {
    margin-top: 36px; font-size: 12.5px; line-height: 1.45;
    color: var(--ink-soft);
  }
  .contact__lines { margin-top: 6px; list-style: none; font-size: 12.5px; color: var(--ink-soft); }
  .contact__lines li { display: flex; align-items: center; gap: 7px; line-height: 1.5; }
  .contact__lines svg { width: 13px; height: 13px; flex: none; }
  .front__rule {
    position: absolute; left: 0; right: 0; bottom: 60px;
    height: 1px; background: var(--rule);
  }
  .front__band {
    position: absolute; left: 0; right: 0; bottom: 0;
    height: 52px; background: var(--band);
  }
  /* Back */
  .card--back {
    background: var(--band); color: var(--paper);
    display: flex; flex-direction: column; align-items: center; justify-content: center;
  }
  .back__name {
    font-weight: 700; font-size: 26px; text-transform: uppercase;
    letter-spacing: 1px; text-align: center; line-height: 1.25;
  }
  .back__web { margin-top: 38px; font-weight: 700; font-size: 15px; letter-spacing: 0.3px; }
</style>
</head>
<body>
<main class="canvas">
  <section class="card card--front" aria-label="Business card front">
    <div class="brand">
      <span class="brand__dot"></span>
      <span class="brand__name">Full Stable Care Vandorpe</span>
    </div>
    <div class="divider"></div>
    <div class="contact">
      <p class="contact__name">Employee Name</p>
      <p class="contact__title">Your Title</p>
      <p class="contact__address">Molkenweg 47<br>B - 2890 Lindenhoven, België</p>
      <ul class="contact__lines">
        <li>
          <svg viewBox="0 0 13 13" aria-hidden="true"><rect width="13" height="13" fill="#111"/><path d="M4 3.2h1.6l.6 1.8-1 .7a5 5 0 0 0 2.2 2.2l.7-1 1.8.6v1.6c0 .4-.3.7-.7.7A6 6 0 0 1 3.3 3.9c0-.4.3-.7.7-.7z" fill="#fff"/></svg>
          + 32 491 68 27 04
        </li>
        <li>
          <svg viewBox="0 0 13 13" aria-hidden="true"><rect width="13" height="13" fill="#111"/><rect x="2.5" y="4" width="8" height="5.5" fill="none" stroke="#fff" stroke-width="1"/><path d="M2.5 4l4 3 4-3" fill="none" stroke="#fff" stroke-width="1"/></svg>
          laurent@fscvandorpe-example.eu
        </li>
      </ul>
    </div>
    <div class="front__rule"></div>
    <div class="front__band"></div>
  </section>

  <section class="card card--back" aria-label="Business card back">
    <p class="back__name">Full Stable Care<br>Vandorpe</p>
    <p class="back__web">fscvandorpe-example.eu</p>
  </section>
</main>
</body>
</html>
```